Corrigan Dwelling Works

We are a building company based in Melbourne Australia. We have a logo but would like to make it a bit more interesting using the same colour scheme of Black, Red and Silver. I have attached our current business card.

Reason: The designs submitted so far are not really what we are looking for. They seem a bit too corporate and we are looking for something a bit funkier.

This is a stationary design I found on the web which we like the look of, something like this using our colours of black, red and silver is what we are looking for.

Cheers

This is our current logo, and front of our business card.

Thanks

Hopefully this example stationery can be viewed to give designers an idea of the look we are hoping for.

Reason: I would like an extra few days for all designers to have the opportunity to submit their designs.

Industry/Entity Type

Building

Colors
eb2027
000000
aaaaaa

```html
<!DOCTYPE html>
<html lang="en">
<head>
<meta charset="utf-8">
<title>Corrigan Dwelling Works – Stationery</title>
<link rel="stylesheet" href="https://fonts.googleapis.com/css2?family=Arimo&family=Quicksand:wght@500&family=Michroma&display=swap">
<style>
:root{
  --black:#000;
  --red:#eb2027;
  --silver:#aaaaaa;
  --silver-light:#c3c5c7;
  --card-grey:#dcdbdc;
  --logo-grey:#9aa4ad;
  --ink:#222;
  --paper:#fff;
  --stage-1:#7a7a7a;
  --stage-2:#444;
}
*{margin:0;padding:0;box-sizing:border-box}
html,body{width:1200px;height:1000px;overflow:hidden}
body{position:relative;background:radial-gradient(ellipse at 60% 20%,var(--stage-1),var(--stage-2));font-family:"Quicksand",sans-serif;color:var(--ink)}
.sheet{position:absolute;box-shadow:2px 3px 6px rgba(0,0,0,.45);overflow:hidden}
.brand-name{font-family:"Arimo",sans-serif;color:var(--logo-grey);white-space:nowrap}
.watermark{position:absolute;font-family:"Arimo",sans-serif;color:#eef0f2;line-height:1;text-align:center}
.contact{position:absolute;font-size:8px;line-height:9.5px;padding-left:6px;border-left:1px solid #555;color:var(--ink)}
.contact li{list-style:none;display:flex;align-items:center;gap:3px}
.contact svg{width:6px;height:6px;fill:var(--red)}
.topbar{position:absolute;left:0;top:0;width:100%}

/* letterhead */
.letterhead{left:30px;top:22px;width:518px;height:669px;background:var(--paper)}
.letterhead .brand-name{position:absolute;left:34px;top:50px;font-size:14px}
.letterhead .contact{left:343px;top:35px}
.letterhead .watermark{left:0;width:100%;top:380px;font-size:46px}
.letterhead .footer{position:absolute;left:0;bottom:0;width:100%;height:22px;background:var(--silver-light);font-size:8px;display:flex;align-items:center;justify-content:center}

/* business card front */
.card-front{left:674px;top:94px;width:425px;height:262px;background:var(--card-grey)}
.card-front .person{position:absolute;left:187px;top:27px}
.card-front .person-name{font-family:"Michroma",sans-serif;font-size:17px;letter-spacing:1.5px;color:#444}
.card-front .person-title{font-size:12px;margin-top:2px;color:var(--ink)}
.card-front .badge{position:absolute;left:32px;top:104px;width:106px;height:54px;background:#2d3d52;border-left:30px solid #f2f0c4}
.card-front .card-contact{position:absolute;left:31px;top:177px;font-size:12.5px;line-height:17px}
.card-front .card-contact span{display:inline-flex;align-items:center;gap:4px;margin-right:8px}
.card-front .card-contact svg{width:10px;height:10px;fill:#111}
.card-front .services{position:absolute;left:0;bottom:0;width:100%;height:38px;background:var(--black);color:#fff;font-size:14px;display:flex;align-items:center;justify-content:center}

/* business card back */
.card-back{left:674px;top:429px;width:425px;height:261px;background:var(--black)}
.card-back .brand-name{position:absolute;left:0;width:100%;text-align:center;top:104px;font-size:30px}
.card-back .address-band{position:absolute;left:0;top:188px;width:100%;height:22px;background:var(--card-grey);color:#111;font-size:15px;display:flex;align-items:center;justify-content:center}

/* envelope */
.envelope{left:81px;top:717px;width:542px;height:263px;background:var(--paper)}
.envelope .brand-name{position:absolute;left:29px;top:36px;font-size:13px}
.envelope .contact{left:29px;top:73px}
.envelope .address{position:absolute;left:29px;top:101px;font-size:7.5px;color:var(--red)}
.envelope .watermark{left:230px;width:260px;top:120px;font-size:34px}
.envelope .footer{position:absolute;left:0;bottom:0;width:100%;height:5px;background:var(--silver-light)}
</style>
</head>
<body>

<svg width="0" height="0" style="position:absolute">
  <defs>
    <symbol id="icon-phone" viewBox="0 0 10 10"><path d="M2 1h2l1 2-1.2 1a6 6 0 0 0 2.2 2.2L7 5l2 1v2c0 .6-.5 1-1 1A8 8 0 0 1 1 2c0-.5.4-1 1-1z"/></symbol>
    <symbol id="icon-fax" viewBox="0 0 10 10"><path d="M3 1h4v3H3zM1 4h8v5H1zM3 6h4v1H3z"/></symbol>
    <symbol id="icon-mail" viewBox="0 0 10 10"><path d="M1 3h8v6H1zM1 3l4 3 4-3" fill="none" stroke="currentColor" stroke-width="1"/></symbol>
  </defs>
</svg>

<section class="sheet letterhead" aria-label="Letterhead">
  <svg class="topbar" viewBox="0 0 518 22" height="22"><polygon points="0,0 395,0 384,22 0,22" fill="var(--black)"/><polygon points="397,0 518,0 518,22 386,22" fill="var(--silver-light)"/></svg>
  <div class="brand-name">Corrigan Dwelling Works</div>
  <ul class="contact">
    <li><svg><use href="#icon-phone"/></svg>0412558907</li>
    <li><svg><use href="#icon-fax"/></svg>95310682</li>
    <li><svg style="color:var(--red)"><use href="#icon-mail"/></svg>dale@corrigandwelling.net.au</li>
  </ul>
  <div class="watermark">Corrigan<br>Dwelling Works</div>
  <div class="footer">PO Box 412, Kelvin Grove VIC 3152</div>
</section>

<section class="sheet card-front" aria-label="Business card front">
  <div class="person">
    <div class="person-name">Dale Fenwick</div>
    <div class="person-title">Master Builder</div>
  </div>
  <div class="badge" role="img" aria-label="Builders association member badge"></div>
  <div class="card-contact">
    <span><svg><use href="#icon-phone"/></svg>0412558907</span><span><svg><use href="#icon-fax"/></svg>95310682</span><br>
    <span><svg style="color:#111"><use href="#icon-mail"/></svg>dale@corrigandwelling.net.au</span>
  </div>
  <div class="services">New Homes Renovations Extensions Project Management</div>
</section>

<section class="sheet card-back" aria-label="Business card back">
  <div class="brand-name">Corrigan Dwelling Works</div>
  <div class="address-band">PO Box 412, Kelvin Grove VIC 3152</div>
</section>

<section class="sheet envelope" aria-label="Envelope">
  <svg class="topbar" viewBox="0 0 542 19" height="19"><polygon points="0,0 401,0 390,19 0,19" fill="var(--black)"/><polygon points="403,0 542,0 542,19 392,19" fill="var(--silver-light)"/></svg>
  <div class="brand-name">Corrigan Dwelling Works</div>
  <ul class="contact">
    <li><svg><use href="#icon-phone"/></svg>0412558907</li>
    <li><svg><use href="#icon-fax"/></svg>95310682</li>
    <li><svg style="color:var(--red)"><use href="#icon-mail"/></svg>dale@corrigandwelling.net.au</li>
  </ul>
  <div class="address">PO Box 412, Kelvin Grove VIC 3152</div>
  <div class="watermark">Corrigan<br>Dwelling Works</div>
  <div class="footer"></div>
</section>

</body>
</html>
```